Plastic Jar Catalogue 7

We are a plastic factory manufacturing different size of plastic jars, which mostly use for spice and grinded coffee. I need the catalogue to be 3 pages:First page: an attractive cover shows the factory's name and logo with a space for products’ picture. Second page: is an items page which I prefer to be enough for 4 items with a space for item number and description under each item. Last page: to be for factory’s address and contact details.

```html
<!DOCTYPE html>
<html lang="en">
<head>
<meta charset="UTF-8">
<title>Crestline Plastic Works – Catalogue 2019</title>
<link rel="stylesheet" href="https://fonts.googleapis.com/css2?family=Montserrat:wght@300;400;600;700;800&family=Hind:wght@400;500&display=swap">
<style>
  :root {
    --red: #e15143;
    --grey-bg: #e5e5e5;
    --panel-grey: #eeeeee;
    --white: #ffffff;
    --teal: #178aa0;
    --ink: #222222;
    --muted: #777777;
    --light-title: #bdbdbd;
  }
  * { margin: 0; padding: 0; box-sizing: border-box; }
  html, body { width: 1200px; height: 675px; overflow: hidden; background: var(--grey-bg); }
  body { position: relative; font-family: "Montserrat", sans-serif; }

  .page { position: absolute; top: 52px; width: 372px; height: 526px; background: var(--white); overflow: hidden; }
  .page--cover { left: 26px; }
  .page--products { left: 414px; }
  .page--contact { left: 804px; }

  /* Cover */
  .cover__side { position: absolute; left: 0; top: 0; width: 207px; height: 100%; background: var(--panel-grey); }
  .cover__band { position: absolute; left: 0; top: 78px; width: 207px; height: 408px; background: var(--red); }
  .cover__photo { position: absolute; left: 91px; top: 171px; width: 262px; height: 223px; background: var(--panel-grey);
    display: flex; align-items: center; justify-content: center; }
  .cover__photo span { color: var(--white); font-weight: 700; font-size: 27px; margin-left: 16px; margin-top: 16px; }
  .brand { position: absolute; display: flex; align-items: center; gap: 6px; color: var(--teal); font-weight: 700; }
  .brand__dot { border-radius: 50%; background: var(--teal); flex: none; }
  .cover__brand { left: 226px; top: 36px; width: 140px; flex-direction: column; text-align: center; gap: 8px; }
  .cover__brand .brand__dot { width: 22px; height: 22px; }
  .cover__brand .brand__name { font-size: 15px; line-height: 1.25; letter-spacing: 1.5px; text-transform: uppercase; }
  .cover__label { position: absolute; left: 28px; top: 399px; color: var(--white); font-weight: 700; font-size: 21px; line-height: 1; }
  .cover__year { position: absolute; left: 35px; top: 424px; color: var(--white); font-weight: 700; font-size: 46px; line-height: 1; letter-spacing: -1px; }

  /* Products */
  .products__frame { position: absolute; left: 21px; top: 46px; width: 338px; height: 456px; border: 1.5px solid var(--red); border-radius: 40px; }
  .products__title { position: absolute; left: 83px; top: 26px; padding: 0 8px; background: var(--white); }
  .products__title h1 { color: var(--red); font-weight: 700; font-size: 24px; line-height: 1.1; }
  .products__title p { color: var(--light-title); font-weight: 300; font-size: 19px; line-height: 1; letter-spacing: 0.5px; }
  .card { position: absolute; width: 134px; height: 148px; border: 1.5px solid var(--red); border-radius: 24px; overflow: hidden; background: var(--white); }
  .card__image { height: 72px; background: var(--panel-grey); border-bottom: 2px solid var(--red);
    display: flex; align-items: center; justify-content: center; color: var(--white); font-family: "Hind", sans-serif; font-size: 12px; padding-top: 10px; }
  .card__body { padding: 4px 6px 0 11px; font-family: "Hind", sans-serif; }
  .card__name { font-family: "Montserrat", sans-serif; color: var(--red); font-weight: 700; font-size: 8px; }
  .card__number { color: var(--teal); font-size: 5.5px; margin: 3px 0 5px 1px; }
  .card__desc { color: var(--ink); font-size: 4.4px; line-height: 1.55; margin-left: 1px; }
  .card--1 { left: 44px; top: 110px; }
  .card--2 { left: 204px; top: 107px; }
  .card--3 { left: 44px; top: 293px; }
  .card--4 { left: 208px; top: 293px; }

  .footer-brand { position: absolute; bottom: 7px; right: 8px; color: var(--ink); font-weight: 700; font-size: 6px; letter-spacing: 0.8px; text-transform: uppercase; text-align: right; line-height: 1.3; gap: 4px; }
  .footer-brand .brand__dot { width: 9px; height: 9px; background: var(--ink); }

  /* Contact */
  .contact__brand { left: 26px; top: 112px; width: 68px; flex-direction: column; text-align: center; gap: 4px; }
  .contact__brand .brand__dot { width: 11px; height: 11px; }
  .contact__brand .brand__name { font-size: 7px; letter-spacing: 0.8px; text-transform: uppercase; line-height: 1.3; }
  .contact__rule { position: absolute; top: 167px; height: 4px; background: var(--red); transform: skewX(-30deg); }
  .contact__rule--short { left: 21px; width: 22px; }
  .contact__rule--long { left: 46px; width: 98px; }
  .contact__details { font-family: "Hind", sans-serif; color: var(--muted); font-size: 7.5px; }
  .contact__address { position: absolute; left: 39px; top: 201px; line-height: 10px; }
  .contact__row { display: flex; gap: 6px; margin-bottom: 9px; }
  .contact__row dt { width: 36px; }
  .contact__place { position: absolute; left: 41px; top: 238px; line-height: 10px; }
  .contact__lines { position: absolute; left: 44px; top: 282px; line-height: 9px; }
  .contact__shadow { position: absolute; left: 217px; top: 112px; width: 150px; height: 331px; background: var(--panel-grey); }
  .contact__panel { position: absolute; left: 221px; top: 99px; width: 151px; height: 336px; background: var(--red); }
</style>
</head>
<body>

<section class="page page--cover">
  <div class="cover__side"></div>
  <div class="cover__band"></div>
  <div class="cover__photo" role="img" aria-label="Photo of plastic spice and coffee jars"><span>IMAGE HERE</span></div>
  <div class="brand cover__brand">
    <span class="brand__dot"></span>
    <span class="brand__name">Crestline Plastic Works</span>
  </div>
  <p class="cover__label">catalogue .</p>
  <p class="cover__year">2019</p>
</section>

<section class="page page--products">
  <div class="products__frame"></div>
  <div class="products__title">
    <h1>Products</h1>
    <p>OVERVIEW</p>
  </div>

  <article class="card card--1">
    <div class="card__image" role="img" aria-label="Product photo of a plastic jar">IMAGE HERE</div>
    <div class="card__body">
      <h2 class="card__name">Product name</h2>
      <p class="card__number">Item number : 656562</p>
      <p class="card__desc">Description : lorem ipsum dolor sit amet, consectetuer adipiscing elit, sed diam nonummy nibh euismod tincidunt ut laoreet dolore magna aliquam erat volutpat. Ut wisi enim ad sed diam nonummy nibh sed diam nonummy nibh sed diam nonummy nibh sed diam nonummy nibh sed diam nonummy</p>
    </div>
  </article>

  <article class="card card--2">
    <div class="card__image" role="img" aria-label="Product photo of a plastic jar">IMAGE HERE</div>
    <div class="card__body">
      <h2 class="card__name">Product name</h2>
      <p class="card__number">Item number : 656562</p>
      <p class="card__desc">Description : lorem ipsum dolor sit amet, consectetuer adipiscing elit, sed diam nonummy nibh euismod tincidunt ut laoreet dolore magna aliquam erat volutpat. Ut wisi enim ad sed diam nonummy nibh sed diam nonummy nibh sed diam nonummy nibh sed diam nonummy nibh sed diam nonummy</p>
    </div>
  </article>

  <article class="card card--3">
    <div class="card__image" role="img" aria-label="Product photo of a plastic jar">IMAGE HERE</div>
    <div class="card__body">
      <h2 class="card__name">Product name</h2>
      <p class="card__number">Item number : 656562</p>
      <p class="card__desc">Description : lorem ipsum dolor sit amet, consectetuer adipiscing elit, sed diam nonummy nibh euismod tincidunt ut laoreet dolore magna aliquam erat volutpat. Ut wisi enim ad sed diam nonummy nibh sed diam nonummy nibh sed diam nonummy nibh sed diam nonummy nibh sed diam nonummy</p>
    </div>
  </article>

  <article class="card card--4">
    <div class="card__image" role="img" aria-label="Product photo of a plastic jar">IMAGE HERE</div>
    <div class="card__body">
      <h2 class="card__name">Product name</h2>
      <p class="card__number">Item number : 656562</p>
      <p class="card__desc">Description : lorem ipsum dolor sit amet, consectetuer adipiscing elit, sed diam nonummy nibh euismod tincidunt ut laoreet dolore magna aliquam erat volutpat. Ut wisi enim ad sed diam nonummy nibh sed diam nonummy nibh sed diam nonummy nibh sed diam nonummy nibh sed diam nonummy</p>
    </div>
  </article>

  <div class="brand footer-brand">
    <span class="brand__dot"></span>
    <span>Crestline<br>Plastic Works</span>
  </div>
</section>

<section class="page page--contact">
  <div class="brand contact__brand">
    <span class="brand__dot"></span>
    <span class="brand__name">Crestline Plastic Works</span>
  </div>
  <div class="contact__rule contact__rule--short"></div>
  <div class="contact__rule contact__rule--long"></div>

  <div class="contact__details">
    <dl class="contact__address">
      <div class="contact__row"><dt>Adress 01 :</dt><dd>Lorem ipsum dolor sit</dd></div>
      <div class="contact__row"><dt>Adress 01 :</dt><dd>Lorem ipsum dolor sit</dd></div>
    </dl>
    <p class="contact__place">City<br>State/Province<br>Coutry</p>
    <p class="contact__lines">+1 - 555-014-2277<br>hello@crestlineworks.com<br>www.crestlineworks.com<br>social: @crestlineworks</p>
  </div>

  <div class="contact__shadow"></div>
  <div class="contact__panel"></div>

  <div class="brand footer-brand">
    <span class="brand__dot"></span>
    <span>Crestline<br>Plastic Works</span>
  </div>
</section>

</body>
</html>
```